Logo & Briefpapier Unternehmer- und Gründerberatung
Zielgruppe
Beratung für die Zielgruppe Unternehmer & Existenzgründer
Aufgabenstellung
Ich benötige ein Logo, Visitenkarte und Briefpapier für mich. Ich bin selbstständig arbeitender Berater für Unternehmer und Existenzgründer. Die Daten sind wie folgt:
Unternehmer- und Gründerberatung
Internet: http://www.beltrumsiedel.com
Anmerkung für die Designer: Das Logo auf der oben angegebenen Webseite ist nur ein Platzhalter und kein Logo-Vorschlag und spiegelt auch nicht meinen Designgeschmack wieder.

```html
<!DOCTYPE html>
<html lang="de">
<head>
<meta charset="utf-8">
<title>Briefpapier – Arno Siedel Unternehmer- und Gründerberatung</title>
<link rel="stylesheet" href="https://fonts.googleapis.com/css2?family=Jost:wght@300;400&family=Barlow+Condensed:wght@300;400&display=swap">
<style>
  :root {
    --backdrop: #ececee;
    --paper: #ffffff;
    --brand-blue: #1467b3;
    --text-grey: #7a7a7a;
    --mark-grey: #9a9a9a;
  }
  * { margin: 0; padding: 0; box-sizing: border-box; }
  html, body { width: 847px; height: 1200px; overflow: hidden; background: var(--backdrop); }
  .sheet {
    position: absolute; left: 90px; top: 132px; width: 692px; height: 980px;
    background: var(--paper); overflow: hidden;
    font-family: "Barlow Condensed", "Arial Narrow", sans-serif;
    font-weight: 300; color: var(--text-grey);
  }
  .brand { position: absolute; left: 419px; top: 65px; width: 221px; height: 34px; }
  .brand-square {
    position: absolute; left: 0; top: 1px; width: 32px; height: 32px;
    border: 3px solid var(--mark-grey); border-radius: 4px;
  }
  .brand-name {
    position: absolute; left: 44px; top: -7px;
    font-family: "Jost", sans-serif; font-weight: 300; font-size: 23px;
    letter-spacing: 0.8px; color: var(--mark-grey); white-space: nowrap; line-height: 30px;
  }
  .brand-tagline {
    position: absolute; left: 44px; top: 23px;
    font-family: "Jost", sans-serif; font-weight: 400; font-size: 9px;
    letter-spacing: 0.1px; color: var(--brand-blue); white-space: nowrap; line-height: 12px;
  }
  .contact-block {
    position: absolute; right: 52px; top: 124px;
    text-align: right; font-size: 8.4px; line-height: 11.2px;
  }
  .contact-block p + p { margin-top: 11.2px; }
  .return-address {
    position: absolute; left: 92px; top: 203px;
    font-size: 6px; color: var(--brand-blue); white-space: nowrap; word-spacing: 0.5px;
  }
  .return-address .sep { margin: 0 4px; }
  .footer-info {
    position: absolute; top: 943px; left: 0; width: 100%;
    font-size: 8.2px; line-height: 11.4px;
  }
  .footer-col { position: absolute; top: 0; white-space: nowrap; }
  .footer-col .label { color: var(--brand-blue); }
  .col-name { left: 54px; } .col-tax { left: 189px; } .col-bank { left: 305px; }
  .col-account { left: 430px; } .col-iban { left: 533px; }
  .footer-band {
    position: absolute; left: 0; bottom: 0; width: 100%; height: 4px;
    background: var(--brand-blue);
  }
</style>
</head>
<body>
  <div class="sheet">
    <div class="brand">
      <span class="brand-square"></span>
      <span class="brand-name">Arno Siedel</span>
      <span class="brand-tagline">UNTERNEHMER- UND GRÜNDERBERATUNG</span>
    </div>

    <div class="contact-block">
      <p>Arno Siedel<br>Unternehmer- und Gründerberatung</p>
      <p>Kastanienweg 14<br>86399 Lindach</p>
      <p>Tel.: 04521 - 36 18 270<br>Fax.: 04521 - 36 18 271</p>
      <p>www.beltrumsiedel.com<br>beratung@beltrumsiedel.com</p>
    </div>

    <div class="return-address">
      ARNO SIEDEL<span class="sep">I</span>Unternehmer- und Gründerberatung<span class="sep">I</span>86399 Lindach
    </div>

    <div class="footer-info">
      <div class="footer-col col-name"><span class="label">Arno Siedel</span><br>Unternehmer- und Gründerberatung</div>
      <div class="footer-col col-tax"><span class="label">Umsatzsteuer ID:</span><br>DE314527809</div>
      <div class="footer-col col-bank"><span class="label">Bankverbindung:</span><br>Sparkasse Talbrücken</div>
      <div class="footer-col col-account">Konto-Nr.: 52083716<br>BLZ: 10020030</div>
      <div class="footer-col col-iban">IBAN: DE00 1002 0030 0052 0837 16<br>BIC: TALBDEX1XXX</div>
    </div>
    <div class="footer-band"></div>
  </div>
</body>
</html>
```